Meadow Voyages Web Page Redesign

IF YOu ARE IN INDIA - PLEASE PLEASE PLEASE - make sure you are working off of MEADOWVOYAGES.COM - Not another site. Look at the URL above when you see the site!

Our website http://www.meadowvoyages.com is driven by a backend database providing content. We are interested in redesigning the website layout to make it responsive and also to make it more interesting, catchy and call to action oriented. Right now it seems not to be able to deliver the message and a little crowded. The main template pages to be addressed are index.aspx, default.aspx, TourList1.aspx, and the actual tour detail page.

There needs to be tight integration / prominent visibility for Social Media.

Focus needs to be on design that would reduce the bounce rate and be SEO friendly.

You will be responsible for layout and delivering the front end css / layout / slices to integrate with the back end.

If you are based in India, you are probably going to be redirected to another site. Please make sure you are working off of MEADOWVOYAGES.COM

Target Market(s)

It is a B2C site - travelers who are interested in traveling to India, Europe and South Africa.

Industry/Entity Type

Media

Font styles to use
Sans Serif

Requirements
Must have
• ONE VERY IMPORTANT POINT : We have a number of photographs that we would love to put online. Unfortunately our current design requires us to resize / crop the photographs which make them lose the impact. We would prefer a design where the images could be used as-is.

Tight integration with Social Media is there in our engine so it should be visible on the website.

Responsive.
Nice to have
• Try using the same color scheme but we are open for changes in the same tone..

```html
<!DOCTYPE html>
<html lang="en">
<head>
<meta charset="utf-8">
<title>Meadow Voyages</title>
<link href="https://fonts.googleapis.com/css2?family=Open+Sans:ital,wght@0,400;0,600;1,400&display=swap" rel="stylesheet">
<style>
:root{
  --red:#8b1414;
  --red-dark:#6e0f0f;
  --red-text:#9a1b1b;
  --gold:#f2c21b;
  --gold-light:#fbdb4d;
  --ink:#1e1e1e;
  --ink-deep:#161616;
  --grey-text:#777;
  --light:#efefef;
  --white:#fff;
  --line:#d9d9d9;
}
*{box-sizing:border-box;margin:0;padding:0}
html,body{width:775px;height:1200px;overflow:hidden;background:var(--white);font-family:"Open Sans",Arial,sans-serif;color:var(--grey-text)}
.page{position:relative;width:775px;height:1200px}
.abs{position:absolute}

/* header */
.site-header{left:0;top:0;width:775px;height:57px;background:var(--ink);border-bottom:3px solid var(--red)}
.brand{left:64px;top:0;width:325px;height:54px;background:linear-gradient(90deg,var(--red-dark),#8e1a1a);display:flex;align-items:center;padding-left:16px;gap:10px}
.brand-dot{width:30px;height:30px;border-radius:50%;background:var(--gold)}
.brand-name{font-size:21px;font-weight:600;color:var(--white);letter-spacing:1px}
.social{display:flex;gap:4px}
.social span{width:18px;height:18px;border-radius:50%;background:#9a9a9a;display:block}
.header-social{left:437px;top:18px}
.header-divider{left:556px;top:8px;width:1px;height:38px;background:#444}
.tollfree{left:571px;top:13px;font-size:9px;color:#bbb;line-height:1.1}
.tollfree strong{display:block;font-size:15px;font-weight:600;color:var(--gold)}
.phone-icon{left:688px;top:20px}

/* hero */
.hero{left:0;top:57px;width:775px;height:331px;background:radial-gradient(ellipse at 45% 40%,#c8801e 0%,#7a3c0a 35%,#2a1406 70%,#120904 100%)}
.hero-caption{left:0;top:330px;width:775px;height:58px;background:rgba(0,0,0,.55);color:var(--white);font-size:11.5px;text-align:center;line-height:18px;padding-top:11px}
.hero-caption em{font-style:normal;color:var(--gold)}
.hero-arrow{top:207px;width:30px;height:30px;background:var(--white);display:flex;align-items:center;justify-content:center}

/* destinations */
.dest{top:410px;width:155px;text-align:center}
.dest h3{font-size:12px;font-weight:600;color:var(--red-text);letter-spacing:.3px;margin-bottom:6px}
.dest .photo{height:95px}
.rule{left:64px;top:537px;width:647px;height:1px;background:var(--line)}

/* welcome */
.welcome{left:66px;top:562px;width:478px}
.welcome h1{font-size:16.5px;font-weight:400;color:var(--red-text);margin-bottom:6px}
.welcome p{font-size:8.6px;line-height:14.7px;margin-bottom:6px}
.promo{left:64px;top:723px;width:479px;height:76px;background:linear-gradient(90deg,#d7d1cb,#f1efee 30%,#e5e1dc 80%,#b9aea1)}
.promo-photo{left:64px;top:723px;width:123px;height:76px;background:linear-gradient(135deg,#b33a26,#c9742d)}
.promo-text{left:195px;top:733px;font-size:12.5px;line-height:18px;color:var(--red-text)}
.btn-dark{left:195px;top:773px;width:54px;height:15px;background:#2b2b2b;border-radius:3px;color:var(--white);font-size:7.5px;text-align:center;line-height:15px}

/* sidebar */
.finder{left:554px;top:567px;width:157px;height:233px;background:var(--red);border-radius:2px;padding:9px 10px}
.finder label{display:block;font-size:9px;color:var(--white);margin-bottom:5px}
.select{height:22px;background:var(--white);border-radius:2px;font-size:9.5px;color:#333;padding:4px 9px;position:relative;margin-bottom:6px}
.select i{position:absolute;right:8px;top:8px;border:5px solid transparent;border-top:6px solid #888}
.finder ul{list-style:none}
.finder li{height:24px;margin-bottom:4.4px;background:linear-gradient(var(--gold-light),var(--gold));border-radius:1px;font-size:10px;font-weight:600;color:#5a1010;line-height:24px;padding-left:21px;position:relative}
.finder li::before{content:"›";position:absolute;left:9px;top:-1px;color:#b8860b;font-weight:400}

/* testimonials */
.testimonials{left:0;top:837px;width:775px;height:167px;background:var(--light);border-top:1px solid #ddd}
.testimonials h2{position:absolute;left:0;top:22px;width:775px;text-align:center;font-size:19px;font-weight:400;color:var(--red-text)}
.avatar{left:82px;top:900px;width:80px;height:80px;border-radius:50%;background:linear-gradient(#d7d3cf,#b9aea4);border:4px solid var(--white);box-shadow:0 1px 4px rgba(0,0,0,.2)}
.quote{left:176px;top:906px;width:520px;font-size:9.3px;font-style:italic;line-height:16.5px;color:#555}
.quote-by{left:176px;top:957px;font-size:9.3px;color:var(--red-text)}
.t-arrow{top:911px}

/* newsletter */
.newsletter{left:0;top:1004px;width:775px;height:60px;background:var(--red)}
.newsletter h2{position:absolute;left:110px;top:17px;font-size:19px;font-weight:400;color:var(--white)}
.field{top:1023px;width:170px;height:22px;background:var(--white);border-radius:2px;font-size:9.5px;color:#333;padding:4px 9px}
.subscribe{left:600px;top:1023px;width:64px;height:22px;background:var(--gold);border-radius:2px;font-size:10px;font-weight:600;color:#3a0a0a;text-align:center;line-height:22px}

/* footer */
.footer{left:0;top:1068px;width:775px;height:84px;background:var(--ink);border-top:3px solid #555}
.footer-col{top:1086px;font-size:8.5px;line-height:17.6px;color:#bbb;list-style:none}
.footer-col.links li::before{content:"•";margin-right:6px;font-size:7px}
.connect{left:598px;top:1090px;font-size:8.5px;color:#bbb}
.footer-social{left:598px;top:1110px}
.copyright{left:0;top:1152px;width:775px;height:48px;background:var(--ink-deep);text-align:center;font-size:8.5px;color:#999;line-height:48px}
</style>
</head>
<body>
<div class="page">

  <header class="site-header abs"></header>
  <div class="brand abs"><span class="brand-dot"></span><span class="brand-name">MEADOW VOYAGES</span></div>
  <div class="social header-social abs"><span></span><span></span><span></span><span></span><span></span></div>
  <div class="header-divider abs"></div>
  <div class="tollfree abs">Toll free from US &amp; Canada<strong>800.555.0142</strong></div>
  <svg class="phone-icon abs" width="18" height="16" viewBox="0 0 24 24"><path fill="#f2c21b" d="M6.6 10.8a15 15 0 0 0 6.6 6.6l2.2-2.2c.3-.3.7-.4 1-.2 1.1.4 2.3.6 3.6.6.6 0 1 .4 1 1V20c0 .6-.4 1-1 1A17 17 0 0 1 3 4c0-.6.4-1 1-1h3.5c.6 0 1 .4 1 1 0 1.3.2 2.5.6 3.6.1.3 0 .7-.2 1z"/></svg>

  <section class="hero abs" role="img" aria-label="Night view of an illuminated hilltop palace above a lake"></section>
  <div class="hero-arrow abs" style="left:0"><svg width="14" height="16"><path d="M11 2 3 8l8 6" stroke="#333" stroke-width="3" fill="none"/></svg></div>
  <div class="hero-arrow abs" style="left:745px"><svg width="14" height="16"><path d="M3 2l8 6-8 6" stroke="#333" stroke-width="3" fill="none"/></svg></div>
  <p class="hero-caption abs">We are the official Representative for all the <em>VELORA</em> trains in spain, and for the tours such as Desert Star Express :<br>A Fortnight of Lanterns, Coastal Odyssey, Royal Dunes Express, and Silver Chariot of India</p>

  <div class="dest abs" style="left:66px"><h3>SPAIN &amp; PORTUGAL</h3><div class="photo" role="img" aria-label="Modern cable-stayed bridge against a blue sky" style="background:linear-gradient(135deg,#1f4fa8,#6e9bd8 60%,#cfd9e6)"></div></div>
  <div class="dest abs" style="left:229px"><h3>INDIA</h3><div class="photo" role="img" aria-label="White marble mausoleum reflected in a pool" style="background:linear-gradient(#4d86c9,#b7cde3 55%,#3f6e9e)"></div></div>
  <div class="dest abs" style="left:392px"><h3>AFRICA</h3><div class="photo" role="img" aria-label="Colourful painted wall with traditional dolls" style="background:linear-gradient(135deg,#c23b2a,#e2b53a 40%,#2f5fa8 75%,#8a3a2a)"></div></div>
  <div class="dest abs" style="left:556px"><h3>SOUTH AMERICA</h3><div class="photo" role="img" aria-label="Ancient mountain ruins under clouds" style="background:linear-gradient(#5e6458,#9a9a86 40%,#6f8a3e)"></div></div>
  <div class="rule abs"></div>

  <main class="welcome abs">
    <h1>Welcome to Meadow Voyages</h1>
    <p>Aliquam scelerisque mauris dui, ut sollicitudin metus feugiat a. Lorem ipsum dolor sit amet, consectetur adipiscing elit. Nam nisl lorem, volutpat eu urna nec, fringilla varius purus. Integer lobortis odio et nulla placerat, a ultricies nisl bibendum. Proin pulvinar porttitor leo, id bibendum massa imperdiet non. Nullam vestibulum erat vitae nisi viverra placerat. Fusce placerat pellentesque ligula, non accumsan nibh sagittis et. Pellentesque molestie, odio at scelerisque vulputate, metus mi facilisis metus, eu sollicitudin lectus sapien rutrum nibh.</p>
    <p>Duis sit amet erat ligula. Ut vitae aliquam mauris. Proin faucibus hendrerit turpis nec vehicula. In ligula erat, fermentum eu justo id, scelerisque dapibus tortor. Aliquam scelerisque mauris dui, ut sollicitudin metus feugiat a. Lorem ipsum dolor sit amet, consectetur adipiscing elit. Nam nisl lorem, volutpat eu urna nec.</p>
  </main>
  <div class="promo abs" role="img" aria-label="Riverside ghats with temples"></div>
  <div class="promo-photo abs" role="img" aria-label="Holy man in orange robes"></div>
  <p class="promo-text abs">Save $200 on Desert Star Express and<br>Royal Dunes Express tours</p>
  <div class="btn-dark abs">Read More</div>

  <aside class="finder abs">
    <label>Select a Place :</label>
    <div class="select">Africa<i></i></div>
    <ul>
      <li>Tour Calendar</li><li>Job Opportunities</li><li>Contact Us</li><li>About Us</li><li>Buy Travel Insurance</li><li>My Account</li>
    </ul>
  </aside>

  <section class="testimonials abs"><h2>TESTIMONIALS</h2></section>
  <svg class="t-arrow abs" style="left:27px" width="12" height="20"><path d="M10 2 2 10l8 8" stroke="#888" stroke-width="2" fill="none"/></svg>
  <svg class="t-arrow abs" style="left:736px" width="12" height="20"><path d="M2 2l8 8-8 8" stroke="#888" stroke-width="2" fill="none"/></svg>
  <div class="avatar abs" role="img" aria-label="Portrait of a smiling traveller"></div>
  <p class="quote abs">“ Nam a malesuada libero. Duis sodales et libero vel interdum. Interdum et malesuada fames ac ante ipsum primis in faucibus. Donec lobortis dui tortor, eu lobortis felis mattis nec. Sed justo quam, luctus eu mauris eget, euismod dapibus sem. Sed tempus feugiat ante, at ornare libero volutpat sed. Maecenas quis magna magna. ”</p>
  <p class="quote-by abs">Daniel - Maple Grove, United States of America</p>

  <section class="newsletter abs"><h2>NEWS LETTER</h2></section>
  <div class="field abs" style="left:250px">Name</div>
  <div class="field abs" style="left:425px">Email ID</div>
  <div class="subscribe abs">Subscribe</div>

  <footer class="footer abs"></footer>
  <ul class="footer-col links abs" style="left:73px"><li>Home</li><li>About us</li><li>Contact us</li></ul>
  <ul class="footer-col links abs" style="left:168px"><li>Employment</li><li>Agents Area</li><li>Site Map</li></ul>
  <ul class="footer-col abs" style="left:277px"><li>14 Elm Row, Fairview, NJ - 07010</li><li>Phone : 609-555-0118</li><li>Fax : 609-555-0118</li></ul>
  <ul class="footer-col abs" style="left:446px"><li>Toll Free : 1-888-555-0164</li><li style="padding-left:41px">1-877-555-0193</li><li>E-mail : info@meadowvoyages.com</li></ul>
  <p class="connect abs">Connect with us</p>
  <div class="social footer-social abs"><span></span><span></span><span></span><span></span><span></span></div>
  <div class="copyright abs">Copyright &nbsp;©&nbsp; 2014 &nbsp; Meadow Voyages. &nbsp;All rights reserved &nbsp; / &nbsp; Terms and Conditions</div>

</div>
</body>
</html>
```